HPS business cards

(Generators . Lighting Towers . De-watering Pumps . Compressors) put under the logo please. my details are Owen Pritchard (Director) 0461527390 harbourpinesupply@postvale.net

```html
<!DOCTYPE html>
<html lang="en">
<head>
<meta charset="utf-8">
<title>HPS Business Cards</title>
<link rel="stylesheet" href="https://fonts.googleapis.com/css2?family=Montserrat:wght@400;500;600;700&display=swap">
<style>
  :root {
    --stage: #2a2a2a;
    --card: #1a1a1a;
    --amber: #d48f2c;
    --steel: #b3b3b3;
    --ink-light: #e6e6e6;
    --rule: #d48f2c;
  }
  * { box-sizing: border-box; margin: 0; padding: 0; }
  html, body { width: 1200px; height: 875px; overflow: hidden; }
  body {
    background: var(--stage);
    font-family: "Montserrat", sans-serif;
    position: relative;
  }
  .card {
    position: absolute;
    top: 282px;
    width: 520px;
    height: 310px;
    background: var(--card);
    border-radius: 16px;
    overflow: hidden;
    box-shadow: 0 18px 40px rgba(0,0,0,0.55);
  }
  .card--front { left: 50px; }
  .card--back { left: 630px; }
  .card__bands { position: absolute; inset: 0; width: 100%; height: 100%; }

  .brand {
    display: flex;
    align-items: center;
    gap: 12px;
    color: var(--amber);
    font-weight: 700;
    letter-spacing: 0.5px;
  }
  .brand__mark {
    background: var(--amber);
    flex: none;
  }

  .card--front .brand {
    position: absolute;
    left: 0; right: 0; top: 112px;
    justify-content: center;
    font-size: 28px;
  }
  .card--front .brand__mark { width: 22px; height: 22px; }
  .services {
    position: absolute;
    left: 0; right: 0; top: 196px;
    text-align: center;
    color: var(--amber);
    font-size: 12.5px;
    font-weight: 600;
    letter-spacing: 0.2px;
  }

  .card--back .brand {
    position: absolute;
    left: 34px; top: 172px;
    flex-direction: column;
    align-items: flex-start;
    gap: 8px;
    font-size: 19px;
    line-height: 1.1;
  }
  .card--back .brand__mark { width: 16px; height: 16px; }
  .divider {
    position: absolute;
    left: 246px; top: 108px;
    width: 1.5px; height: 112px;
    background: var(--rule);
  }
  .contact {
    position: absolute;
    left: 264px; top: 104px;
    color: var(--ink-light);
  }
  .contact__name { color: var(--amber); font-size: 20px; font-weight: 700; }
  .contact__role { font-size: 12px; font-weight: 500; margin: 2px 0 12px; }
  .contact__line {
    display: flex; align-items: center; gap: 7px;
    font-size: 11.5px; margin-bottom: 5px;
  }
  .contact__icon { width: 11px; height: 11px; flex: none; }
</style>
</head>
<body>

<section class="card card--front">
  <svg class="card__bands" viewBox="0 0 520 310" preserveAspectRatio="none" aria-hidden="true">
    <polygon points="0,0 220,0 206,16 0,16" fill="var(--amber)"/>
    <polygon points="232,0 520,0 520,16 218,16" fill="var(--steel)"/>
    <polygon points="0,294 330,294 316,310 0,310" fill="var(--amber)"/>
    <polygon points="344,294 520,294 520,310 330,310" fill="var(--steel)"/>
  </svg>
  <div class="brand">
    <span class="brand__mark"></span>
    <span class="brand__name">HARBOUR PINE SUPPLY</span>
  </div>
  <p class="services">Generators . Lighting Towers . De-watering Pumps . Compressors</p>
</section>

<section class="card card--back">
  <svg class="card__bands" viewBox="0 0 520 310" preserveAspectRatio="none" aria-hidden="true">
    <polygon points="0,0 200,0 186,16 0,16" fill="var(--amber)"/>
    <polygon points="212,0 520,0 520,16 198,16" fill="var(--steel)"/>
    <polygon points="0,294 370,294 356,310 0,310" fill="var(--amber)"/>
    <polygon points="384,294 520,294 520,310 370,310" fill="var(--steel)"/>
  </svg>
  <div class="brand">
    <span class="brand__mark"></span>
    <span class="brand__name">HARBOUR PINE<br>SUPPLY</span>
  </div>
  <div class="divider"></div>
  <div class="contact">
    <p class="contact__name">Owen Pritchard</p>
    <p class="contact__role">Director</p>
    <p class="contact__line">
      <svg class="contact__icon" viewBox="0 0 24 24"><path fill="var(--amber)" d="M6.6 10.8a15.1 15.1 0 0 0 6.6 6.6l2.2-2.2c.3-.3.7-.4 1-.2 1.1.4 2.3.6 3.6.6.6 0 1 .4 1 1V20c0 .6-.4 1-1 1A17 17 0 0 1 3 4c0-.6.4-1 1-1h3.5c.6 0 1 .4 1 1 0 1.3.2 2.5.6 3.6.1.3 0 .7-.2 1z"/></svg>
      <span>0461527390</span>
    </p>
    <p class="contact__line">
      <svg class="contact__icon" viewBox="0 0 24 24"><path fill="var(--amber)" d="M2 5h20v14H2z"/><path fill="none" stroke="var(--card)" stroke-width="2" d="M2 5l10 8 10-8"/></svg>
      <span>harbourpinesupply@postvale.net</span>
    </p>
    <p class="contact__line">
      <svg class="contact__icon" viewBox="0 0 24 24"><circle cx="12" cy="12" r="10" fill="none" stroke="var(--amber)" stroke-width="2.5"/><path fill="none" stroke="var(--amber)" stroke-width="2" d="M2 12h20M12 2c3 3 3 17 0 20M12 2c-3 3-3 17 0 20"/></svg>
      <span>harbourpinesupply.com</span>
    </p>
  </div>
</section>

</body>
</html>
```